Singapore Peer-to-Peer Business Loans Site Needs a Name Card Design

We need a name card design for a new company based in Singapore called 'Ledgerbloom Capital (Singapore) Pte. Ltd.' or in short, 'LedbolSG'.
We run an online platform where small and medium enterprises can access seed capital from wealthy persons seeking high yield returns.
We need a name card design - We would like to see designs that use the colours red, black and/or grey, using any combination of the logos that we have attached. The final design should communicate transparency, innovativeness, financial savvy, and professionalism.
Target Market(s)
Sophisticated/expert financial investors and small & medium business owners.
Industry/Entity Type
Financial

```html
<!DOCTYPE html>
<html lang="en">
<head>
<meta charset="utf-8">
<title>LedbolSG Name Card</title>
<link rel="stylesheet" href="https://fonts.googleapis.com/css2?family=Source+Sans+3:wght@400;700&display=swap">
<style>
  :root {
    --ink: #231f20;
    --brand-dark: #323a41;
    --brand-red: #e32628;
    --paper: #ffffff;
    --frame: #231f20;
  }
  * { box-sizing: border-box; margin: 0; padding: 0; }
  html, body {
    width: 1200px; height: 1200px; overflow: hidden;
    background: var(--paper);
    font-family: "Source Sans 3", "Myriad Pro", Arial, sans-serif;
    color: var(--ink);
  }
  .canvas { position: relative; width: 1200px; height: 1200px; }
  .card {
    position: absolute; left: 110px; width: 1001px; height: 586px;
    border: 3px solid var(--frame); background: var(--paper);
  }
  .card--front { top: 8px; }
  .card--back { top: 607px; }

  .wordmark {
    position: absolute; display: flex; align-items: center;
    font-weight: 700; color: var(--brand-dark); line-height: 1;
    letter-spacing: -1px;
  }
  .wordmark__dot { background: var(--brand-red); flex: none; }
  .card--front .wordmark { right: 26px; top: 110px; font-size: 104px; gap: 22px; }
  .card--front .wordmark__dot { width: 56px; height: 56px; }
  .card--back .wordmark { left: 64px; right: 64px; top: 148px; justify-content: center; font-size: 176px; gap: 36px; }
  .card--back .wordmark__dot { width: 96px; height: 96px; }

  .person { position: absolute; right: 20px; top: 300px; text-align: right; line-height: 1.15; }
  .person__name { font-size: 45px; }
  .person__direct { font-size: 39px; }
  .label { font-weight: 700; }

  .contact {
    position: absolute; right: 18px; top: 478px;
    display: flex; align-items: stretch; font-size: 27px; line-height: 36px;
  }
  .contact__address { text-align: right; padding-right: 12px; }
  .contact__divider { width: 3px; background: var(--brand-red); margin: 6px 0 4px; }
  .contact__online { padding-left: 12px; }
</style>
</head>
<body>
<main class="canvas">
  <section class="card card--front">
    <div class="wordmark"><span class="wordmark__dot"></span><span>LedbolSG</span></div>
    <div class="person">
      <p class="person__name"><span class="label">Name:</span> Daniel Tan</p>
      <p class="person__direct"><span class="label">Direct:</span> +65 6100 2345</p>
    </div>
    <div class="contact">
      <div class="contact__address">
        <p><span class="label">Address:</span> 18 Harbour Lane,</p>
        <p>#14-00 Meridian Tower Centre, Singapore 049321</p>
      </div>
      <span class="contact__divider"></span>
      <div class="contact__online">
        <p><span class="label">Email:</span> contact@ledbol.sg</p>
        <p><span class="label">Website:</span> www.ledbol.sg</p>
      </div>
    </div>
  </section>

  <section class="card card--back">
    <div class="wordmark"><span class="wordmark__dot"></span><span>LedbolSG</span></div>
  </section>
</main>
</body>
</html>
```